Business card design for Medical Practice Mgmt company
Ashfield Clinic Allies
Business card design for Medical Practice Mgmt company - Medical
Creative Brief
Professional
Monica Daltrey
VP of Operations
4170 E Holloway Ln # 210 Plano, TX 75041
mdaltrey@aca-mail.net
www.ashfieldclinicallies.net
jdovan jdovan
uploaded AI file
bluefern bluefern
Logo Ai file needed!

```html
<!DOCTYPE html>
<html lang="en">
<head>
<meta charset="utf-8">
<title>Ashfield Clinic Allies – Business Card</title>
<link href="https://fonts.googleapis.com/css2?family=Montserrat:wght@400;500;600&family=Open+Sans:wght@400;600&display=swap" rel="stylesheet">
<style>
  :root{
    --page:#e9e7e4;
    --ink:#2a2f3a;
    --brand-blue:#2f8fd0;
    --card-white:#ffffff;
    --card-black:#0b0b0b;
    --muted:#4b5563;
    --stripe-light:#9fcbe8;
  }
  *{margin:0;padding:0;box-sizing:border-box}
  html,body{width:1200px;height:988px;overflow:hidden;background:var(--page)}
  .canvas{position:relative;width:1200px;height:988px}
  .card{position:absolute;left:220px;width:760px;height:434px;border-radius:4px;
    box-shadow:0 10px 28px rgba(0,0,0,.18);overflow:hidden}

  /* back */
  .card-back{top:40px;background:var(--card-black)}
  .back-mark{position:absolute;left:50%;top:150px;transform:translateX(-50%);
    display:flex;align-items:center;gap:14px}
  .back-mark .dot{width:70px;height:70px;border-radius:50%;background:var(--brand-blue)}
  .back-mark .name{font-family:"Montserrat",sans-serif;font-weight:500;font-size:26px;color:#fff}
  .back-url{position:absolute;bottom:46px;width:100%;text-align:center;
    font-family:"Open Sans",sans-serif;font-size:18px;letter-spacing:4px;color:#fff}

  /* front */
  .card-front{top:514px;background:var(--card-white)}
  .logo{position:absolute;top:42px;left:0;width:100%;text-align:center}
  .logo-row{display:inline-flex;align-items:center;gap:12px}
  .logo .dot{width:30px;height:30px;border-radius:50%;background:var(--brand-blue)}
  .logo .name{font-family:"Montserrat",sans-serif;font-weight:500;font-size:38px;color:var(--ink);letter-spacing:1px}
  .tagline{margin-top:8px;font-family:"Open Sans",sans-serif;font-size:11px;color:var(--brand-blue)}

  .details{position:absolute;top:188px;left:178px;font-family:"Open Sans",sans-serif;
    font-size:13px;color:var(--muted);line-height:1.55}
  .details .person{color:var(--brand-blue);font-weight:600;font-size:15px}
  .contacts{position:absolute;top:184px;left:400px;list-style:none;font-family:"Open Sans",sans-serif;
    font-size:13px;color:var(--muted)}
  .contacts li{display:flex;align-items:center;gap:8px;height:21px}
  .contacts svg{width:14px;height:14px;flex:none}

  .rule{position:absolute;left:0;width:100%}
  .rule-thin{top:344px;height:2px;background:var(--stripe-light)}
  .rule-blue{top:352px;height:4px;background:var(--brand-blue)}
  .band{position:absolute;top:362px;left:0;width:100%;height:48px;background:var(--card-black);
    display:flex;align-items:center;justify-content:center;
    font-family:"Open Sans",sans-serif;font-size:21px;letter-spacing:4px;color:#fff}
  .rule-bottom{top:416px;height:3px;background:var(--stripe-light)}
</style>
</head>
<body>
<main class="canvas">
  <section class="card card-back">
    <div class="back-mark"><span class="dot"></span><span class="name">Ashfield Clinic Allies</span></div>
    <p class="back-url">www.ashfieldclinicallies.net</p>
  </section>

  <section class="card card-front">
    <div class="logo">
      <div class="logo-row"><span class="dot"></span><span class="name">Ashfield Clinic Allies</span></div>
      <p class="tagline">Practice management and consulting for physician groups</p>
    </div>

    <div class="details">
      <p class="person">Monica Daltrey</p>
      <p>VP of Operations</p>
      <p>4170 E Holloway Ln</p>
      <p># 210 Plano, TX 75041</p>
    </div>

    <ul class="contacts">
      <li><svg viewBox="0 0 14 14"><circle cx="7" cy="7" r="7" fill="#2f8fd0"/><path d="M4.5 3.5l1.6 0 .5 2-1 .7a5 5 0 0 0 2.2 2.2l.7-1 2 .5v1.6c-3.5.3-6.3-2.5-6-6z" fill="#fff"/></svg>469-555-0151</li>
      <li><svg viewBox="0 0 14 14"><circle cx="7" cy="7" r="7" fill="#2f8fd0"/><path d="M4.5 3.5l1.6 0 .5 2-1 .7a5 5 0 0 0 2.2 2.2l.7-1 2 .5v1.6c-3.5.3-6.3-2.5-6-6z" fill="#fff"/></svg>469-555-0225</li>
      <li><svg viewBox="0 0 14 14"><circle cx="7" cy="7" r="7" fill="#2f8fd0"/><rect x="4" y="5" width="6" height="5" fill="#fff"/><rect x="5" y="3" width="4" height="2" fill="#fff"/></svg>469-555-0152</li>
      <li><svg viewBox="0 0 14 14"><circle cx="7" cy="7" r="7" fill="#2f8fd0"/><rect x="3.5" y="4.5" width="7" height="5" fill="#fff"/><path d="M3.5 4.5l3.5 3 3.5-3" stroke="#2f8fd0" fill="none"/></svg>mdaltrey@aca-mail.net</li>
    </ul>

    <div class="rule rule-thin"></div>
    <div class="rule rule-blue"></div>
    <div class="band">www.ashfieldclinicallies.net</div>
    <div class="rule rule-bottom"></div>
  </section>
</main>
</body>
</html>
```